Bright Volley Pickleball Tournament

Design a poster for the Copper Ridge Dink Series, a pickleball tournament series. Each event will have it's own poster with a different design. The posters should be different but related graphically. The first assignment is Posters 1 and 2. The posters should be bold, exciting, fun and show movement. The attached files are for content, hierarchy for text but not design. Logo typeface: Legend 54. Logo blue: cmyk blue: 2b3990 R: 43 G:57 B:144
Please contact me with questions.

```html
<!DOCTYPE html>
<html lang="en">
<head>
<meta charset="utf-8">
<title>Bright Volley Pickleball Tournament</title>
<link rel="stylesheet" href="https://fonts.googleapis.com/css2?family=Oswald:wght@600;700&family=Saira+Semi+Condensed:wght@700;800&family=Arimo:ital,wght@0,400;0,700;1,400&display=swap">
<style>
  :root {
    --page: #e4e4e2;
    --navy-deep: #221f5e;
    --navy: #2b3990;
    --violet: #6a2c8f;
    --magenta: #8a3aa8;
    --red-light: #e0342f;
    --red: #b8141b;
    --red-dark: #6e0b10;
    --yellow: #f5d315;
    --orange: #f2a33a;
    --white: #ffffff;
    --soft: #d9dcf2;
  }
  * { box-sizing: border-box; margin: 0; padding: 0; }
  html, body { width: 1008px; height: 1200px; overflow: hidden; }
  body { background: var(--page); position: relative; font-family: "Arimo", Arial, sans-serif; }

  .poster {
    position: absolute; left: 58px; top: 50px; width: 892px; height: 1100px;
    overflow: hidden; color: var(--white);
    background: radial-gradient(ellipse at 55% 40%, var(--navy) 0%, #28307e 45%, var(--navy-deep) 100%);
  }
  .decor { position: absolute; inset: 0; }

  .paddles {
    position: absolute; left: 120px; top: 300px; width: 660px; height: 520px;
    border-radius: 50%;
    background: radial-gradient(ellipse, rgba(150,160,230,.22) 0%, rgba(150,160,230,0) 70%);
  }

  .brand { position: absolute; top: 30px; left: 0; width: 100%; text-align: center; }
  .brand-mark {
    width: 84px; height: 84px; border-radius: 50%; background: var(--yellow);
    margin: 0 auto 16px;
  }
  .brand-name {
    font-family: "Oswald", sans-serif; font-weight: 700; color: var(--white);
    text-transform: uppercase; line-height: 1; letter-spacing: 1px;
  }
  .brand-name .line1 { display: block; font-size: 64px; }
  .brand-name .line2 { display: block; font-size: 44px; margin-top: 6px; }

  .title {
    position: absolute; top: 290px; left: 0; width: 100%; text-align: center;
    font-family: "Oswald", sans-serif; font-weight: 700; font-size: 118px;
    line-height: 1; letter-spacing: 4px; text-transform: uppercase;
    background: linear-gradient(180deg, var(--red-light) 0%, var(--red) 55%, var(--red-dark) 100%);
    -webkit-background-clip: text; background-clip: text; color: transparent;
  }

  .date {
    position: absolute; top: 452px; width: 100%; text-align: center;
    font-family: "Saira Semi Condensed", sans-serif; font-weight: 800;
    font-size: 44px; letter-spacing: 1px; line-height: 1;
  }
  .date-note {
    position: absolute; top: 508px; width: 100%; text-align: center;
    font-size: 29px; line-height: 1;
  }

  .badge {
    position: absolute; left: 351px; top: 566px; width: 160px; height: 96px;
    border-radius: 50%; background: var(--soft); border: 3px solid var(--white);
  }

  .subtitle {
    position: absolute; top: 712px; width: 100%; text-align: center;
    font-family: "Saira Semi Condensed", sans-serif; font-weight: 700;
    font-size: 23px; letter-spacing: .5px; text-transform: uppercase;
  }

  .features { position: absolute; top: 765px; left: 0; width: 100%; height: 146px; }
  .feature {
    position: absolute; top: 0; width: 146px; height: 146px; border-radius: 50%;
    border: 3px solid var(--orange); background: rgba(40,44,120,.85);
    display: flex; align-items: center; justify-content: center; text-align: center;
    font-weight: 700; font-size: 18px; line-height: 1.4; padding: 10px;
  }
  .feature:nth-child(1) { left: 55px; }
  .feature:nth-child(2) { left: 252px; }
  .feature:nth-child(3) { left: 458px; }
  .feature:nth-child(4) { left: 656px; }

  .sponsors {
    position: absolute; top: 928px; width: 100%; text-align: center;
    font-weight: 700; font-size: 20px;
  }
  .contact-bar {
    position: absolute; left: 51px; top: 961px; width: 750px; height: 58px;
    border-radius: 29px; text-align: center; font-size: 18px; line-height: 1.3;
    padding-top: 4px; border: 1px solid rgba(255,255,255,.6);
    background: linear-gradient(180deg, var(--red-light) 0%, var(--red) 55%, var(--red-dark) 100%);
  }
  .contact-bar strong { font-weight: 700; }

  .venue {
    position: absolute; top: 1042px; width: 100%; text-align: center;
    font-size: 15px; line-height: 1.55; color: var(--soft);
  }
  .venue em { display: block; }
</style>
</head>
<body>
<main class="poster">
  <svg class="decor" width="892" height="1100" viewBox="0 0 892 1100" aria-hidden="true">
    <circle cx="760" cy="90" r="85" fill="var(--violet)" opacity=".55"/>
    <circle cx="650" cy="70" r="22" fill="var(--magenta)" opacity=".6"/>
    <circle cx="860" cy="330" r="40" fill="var(--magenta)" opacity=".45"/>
    <circle cx="610" cy="400" r="90" fill="var(--violet)" opacity=".35"/>
    <circle cx="60" cy="990" r="110" fill="var(--violet)" opacity=".5"/>
    <circle cx="830" cy="980" r="70" fill="var(--violet)" opacity=".45"/>
  </svg>
  <div class="paddles" role="img" aria-label="Faint crossed pickleball paddles in the background"></div>

  <header class="brand">
    <div class="brand-mark"></div>
    <h2 class="brand-name"><span class="line1">Copper Ridge</span><span class="line2">Dink Series</span></h2>
  </header>

  <h1 class="title">Bright Volley</h1>
  <p class="date">NOVEMBER 23-24 2019</p>
  <p class="date-note">the weekend before Thanksgiving</p>

  <div class="badge" role="img" aria-label="Sanctioned event badge"></div>

  <p class="subtitle">NPLA Sanctioned Pickleball Tournament</p>

  <ul class="features">
    <li class="feature">Women’s,<br>Men’s &amp; Mixed<br>Doubles</li>
    <li class="feature">3.0, 3.5,<br>4.0, 4.5, 5.0<br>Brackets</li>
    <li class="feature">Cash<br>Prizes!</li>
    <li class="feature">Vantaflex<br>Yellow Indoor<br>Ball</li>
  </ul>

  <p class="sponsors">Sponsorship Opportunities Available</p>
  <div class="contact-bar">
    Questions: <strong>copperridgedinks@rallymail.com</strong><br>
    Registration: <strong>http://courtdrawsheet.com/</strong>
  </div>

  <p class="venue">Meadowline Sportsplex, 210 Harbor Ave, Eastbrook, MA<em>Venue of the 2019 NPLA Atlantic Regional</em></p>
</main>
</body>
</html>
```